Design KWN's Corporate Christmas Card

This project is to design a highly attractive and professional looking corporate Christmas card. The card is A5 size (folded into two halves of A6 either portrait or landscape) plus an A6 matching envelope. The card will be printed in-house onto white matt or pearlised white or cream card stock with matching envelope. The printing will be through a 1200x1200 good-quality colour laser printer. Just to clarify, the cards are A5 size folded into two. The envelopes are A6 size (or slightly larger) to accommodate the card.

The inside of the card will be individually personalised as follows:

KWN wishes
> of

Merry Christmas
and a
Happy New Year

The text in > will be personalised through the mail merge process to our database.

The outside of the card must have either a picture or a graphic or combination that is attractive and professional.

The major criteria for this project are:

* ability to look professional even when printed on normal card stock and office laser printer
* attractiveness
* professionalism
* good corporate identity

Our company logo is attached. Attached are also samples of 6x cards we have seen that are good (YES) and 1x that is bad (NO). Bad in the sense that because we are using normal card stock and office laser printer (albeit good quality printer) the colour will not come out looking good. Please do not incorporate any metallic gilting because the printer will not be able to do that. Also please do not design to the very edge of the paper because the printer won't print to the edge.

Many thanks and best of luck.

```html
<!DOCTYPE html>
<html lang="en">
<head>
<meta charset="utf-8">
<title>KWN Corporate Christmas Card</title>
<link rel="stylesheet" href="https://fonts.googleapis.com/css2?family=Arimo&family=Cormorant+Garamond:wght@500&family=Princess+Sofia&display=swap">
<style>
  :root {
    --page: #ffffff;
    --rule: #222222;
    --ink: #1a1a1a;
    --brand-blue: #0ba9e4;
    --frost-light: #bdeefc;
    --frost: #5fd3f3;
    --greeting-teal: #2aa79b;
  }
  * { margin: 0; padding: 0; box-sizing: border-box; }
  html, body { width: 748px; height: 1200px; overflow: hidden; background: var(--page); }
  .canvas { position: relative; width: 748px; height: 1200px; }

  .view-label {
    position: absolute; left: 0; width: 731px; text-align: center;
    font-family: "Arimo", sans-serif; font-size: 16px; color: var(--ink);
  }
  .view-label--outer { top: 36px; }
  .view-label--inside { top: 628px; }

  .spread {
    position: absolute; left: 37px; width: 660px; height: 467px;
    border: 1px solid var(--rule); display: flex;
  }
  .spread--outer { top: 70px; }
  .spread--inside { top: 676px; }
  .panel { position: relative; width: 50%; height: 100%; }
  .panel + .panel { border-left: 1px solid var(--rule); }

  .brand {
    position: absolute; left: 63px; top: 184px;
    display: flex; align-items: center; gap: 12px;
  }
  .brand-square { width: 40px; height: 40px; background: var(--brand-blue); }
  .brand-name {
    font-family: "Arimo", sans-serif; font-size: 56px; letter-spacing: 8px;
    color: var(--brand-blue); line-height: 1;
  }

  .tree-artwork {
    position: absolute; left: 25px; top: 38px; width: 278px; height: 324px;
  }
  .season-greeting {
    position: absolute; left: 0; width: 100%; top: 382px; text-align: center;
    font-family: "Princess Sofia", cursive; font-size: 31px; color: var(--greeting-teal);
  }

  .inside-message { position: absolute; left: 0; width: 100%; text-align: center; color: var(--ink); }
  .sender { top: 52px; font-family: "Cormorant Garamond", serif; font-size: 14px; }
  .recipient { top: 82px; font-family: "Cormorant Garamond", serif; font-size: 17px; }
  .wish-line { font-family: "Princess Sofia", cursive; line-height: 1; }
  .wish-merry { top: 152px; font-size: 40px; word-spacing: 10px; }
  .wish-and { top: 218px; font-size: 25px; word-spacing: 10px; }
  .wish-year { top: 270px; font-size: 40px; word-spacing: 10px; }
  .flourish { position: absolute; left: 68px; top: 350px; width: 194px; height: 24px; }
</style>
</head>
<body>
<main class="canvas">
  <p class="view-label view-label--outer">Outer</p>
  <section class="spread spread--outer">
    <div class="panel panel--back">
      <div class="brand">
        <span class="brand-square"></span>
        <span class="brand-name">KWN</span>
      </div>
    </div>
    <div class="panel panel--front">
      <svg class="tree-artwork" role="img" aria-label="Christmas tree formed from scattered light blue snowflakes" viewBox="0 0 278 324">
        <defs>
          <linearGradient id="frostFill" x1="0" y1="0" x2="0" y2="1">
            <stop offset="0" stop-color="var(--frost-light)"/>
            <stop offset="1" stop-color="var(--frost)"/>
          </linearGradient>
        </defs>
        <polygon points="139,0 278,290 0,290" fill="url(#frostFill)" opacity="0.55"/>
      </svg>
      <p class="season-greeting">Season's Greetings</p>
    </div>
  </section>

  <p class="view-label view-label--inside">Inside</p>
  <section class="spread spread--inside">
    <div class="panel panel--blank"></div>
    <div class="panel panel--message">
      <p class="inside-message sender">KWN wishes</p>
      <p class="inside-message recipient">Databased Name</p>
      <p class="inside-message wish-line wish-merry">Merry Chrismas</p>
      <p class="inside-message wish-line wish-and">and a</p>
      <p class="inside-message wish-line wish-year">Happy New Year</p>
      <svg class="flourish" role="img" aria-label="Decorative black scroll divider" viewBox="0 0 194 24">
        <rect x="0" y="8" width="194" height="8" rx="4" fill="#555555" opacity="0.35"/>
      </svg>
    </div>
  </section>
</main>
</body>
</html>
```